Biz Card for Harrowfield Property Partners - HWPP

Harrowfield Property Partners is a commercial real estate acquisitions firm. We buy commercial property and need to raise capital from investors for each deal we buy. The vibe needs to be: give us your money, we will multiply it.
Our website: www.hrwpp-example.com
Competitors are: https://velmarholdings-example.com/, https://tribanquepartners-example.com/, http://www.ostrellecapital-example.com/
Target Market(s)
High Net Worth Individuals, Bankers, Insurance Companies, Commercial Real Estate Brokers.
Industry/Entity Type
Investment Banking
Contact Information for Business Card
Name, Title, Addess, Cell#, Office#, email, website
Requirements
Must have
- use one of our logos. See website for look and feel: www.hrwpp-example.com
Nice to have
- see website: www.hrwpp-example.com

```html
<!DOCTYPE html>
<html lang="en">
<head>
<meta charset="utf-8">
<title>Harrowfield Property Partners – Business Card</title>
<link rel="stylesheet" href="https://fonts.googleapis.com/css2?family=Montserrat:wght@400;500&family=Roboto:wght@400;700&display=swap">
<style>
  :root {
    --navy: #0b2540;
    --ink: #141414;
    --paper: #ffffff;
    --backdrop: #e7e4e0;
    --muted: #3a3f46;
  }
  * { margin: 0; padding: 0; box-sizing: border-box; }
  html, body { width: 1200px; height: 909px; overflow: hidden; }
  body {
    background: var(--backdrop);
    font-family: "Roboto", Arial, sans-serif;
    position: relative;
  }
  .card {
    position: absolute;
    width: 540px;
    height: 309px;
    box-shadow: 0 6px 18px rgba(0,0,0,0.18);
    overflow: hidden;
  }
  /* Back of card */
  .card-back {
    left: 50px; top: 110px;
    background: var(--navy);
    display: flex; align-items: center; justify-content: center;
  }
  .back-mark {
    width: 140px; height: 140px; border-radius: 50%;
    background: var(--paper);
    display: flex; align-items: center; justify-content: center;
  }
  .back-mark-name {
    font-family: "Montserrat", Arial, sans-serif;
    font-weight: 500; font-size: 26px; letter-spacing: 4px;
    color: var(--navy);
  }
  /* Front of card */
  .card-front {
    left: 610px; top: 470px;
    background: var(--paper);
  }
  .front-wave { position: absolute; inset: 0; }
  .brand {
    position: absolute; right: 40px; top: 22px;
    display: flex; align-items: center; gap: 12px;
  }
  .brand-dot {
    width: 46px; height: 46px; border-radius: 50%;
    background: var(--navy);
  }
  .brand-name {
    font-family: "Montserrat", Arial, sans-serif;
    font-weight: 500; color: var(--navy);
    font-size: 15px; letter-spacing: 3px; line-height: 1.35;
  }
  .brand-name .sub { display: block; font-size: 8px; letter-spacing: 3.2px; }
  .accent-block {
    position: absolute; right: 0; top: 84px;
    width: 14px; height: 30px; background: var(--navy);
  }
  .person {
    position: absolute; right: 40px; top: 82px; text-align: right;
  }
  .person-name {
    font-weight: 700; font-size: 21px; line-height: 1.2; color: var(--navy); letter-spacing: 0.2px;
  }
  .person-title { font-size: 12px; line-height: 1.3; color: var(--muted); }
  .contact {
    position: absolute; left: 120px; bottom: 14px;
    color: var(--paper); font-size: 11.5px; line-height: 1.35;
    list-style: none;
  }
  .contact .address { margin-bottom: 5px; }
  .contact li { display: flex; align-items: center; gap: 6px; }
  .contact svg { width: 10px; height: 10px; fill: var(--paper); flex: none; }
</style>
</head>
<body>

  <section class="card card-back" aria-label="Card back">
    <div class="back-mark"><span class="back-mark-name">HWPP</span></div>
  </section>

  <section class="card card-front" aria-label="Card front">
    <svg class="front-wave" viewBox="0 0 540 309" preserveAspectRatio="none" aria-hidden="true">
      <path d="M0,309 L0,235 C60,180 150,165 280,165 C390,165 470,165 540,130 L540,309 Z" fill="var(--navy)"/>
      <path d="M20,222 C80,168 170,151 285,152 C395,153 470,152 522,130 C470,158 395,161 285,160 C170,159 90,174 20,222 Z" fill="var(--ink)"/>
    </svg>

    <div class="brand">
      <span class="brand-dot"></span>
      <span class="brand-name">HARROWFIELD<span class="sub">PROPERTY PARTNERS</span></span>
    </div>
    <span class="accent-block"></span>
    <div class="person">
      <p class="person-name">DORIAN KESSLER</p>
      <p class="person-title">Owner/Founder</p>
    </div>

    <ul class="contact">
      <li class="address">4180 Meridian Ave. 1210<br>Lake Halston 02</li>
      <li><svg viewBox="0 0 10 10"><path d="M2,0.5 L4,2.8 L3,4 C3.8,5.6 4.6,6.4 6,7 L7.2,6 L9.5,8 L8,9.6 C4,9 1,6 0.4,2 Z"/></svg>555-014-2290</li>
      <li><svg viewBox="0 0 10 10"><path d="M2.5,0 H7.5 V10 H2.5 Z M3.3,1 V8 H6.7 V1 Z" fill-rule="evenodd"/></svg>555-017-6634</li>
      <li><svg viewBox="0 0 10 10"><path d="M0,2 H10 V8 H0 Z M0.8,2.6 L5,5.6 L9.2,2.6 Z" fill-rule="evenodd"/></svg>info@hrwpp-example.com</li>
      <li><svg viewBox="0 0 10 10"><circle cx="5" cy="5" r="4.5"/></svg>www.hrwpp-example.com</li>
    </ul>
  </section>

</body>
</html>
```